Building Company Business Card Design

I am looking to get a business card designed for my Building Company. Please find the logo attached.

Industry/Entity Type

Business

Contact Information for Business Card

Mobile 0472 913 046
Email admin@tarrowconstructworks.com.au
Website www.tarrowconstructworks.com.au

Colors
0255a3

```html
<!DOCTYPE html>
<html lang="en">
<head>
<meta charset="utf-8">
<title>Tarrow Construct Works – Business Card</title>
<link rel="stylesheet" href="https://fonts.googleapis.com/css2?family=Roboto:wght@400;500&family=Roboto+Condensed:wght@500;700&display=swap">
<style>
  :root {
    --bg: #e9e7e4;
    --slate: #6a6b6f;
    --slate-light: #76777b;
    --brand-blue: #1452a0;
    --paper: #f4f4f4;
    --white: #ffffff;
    --ink-grey: #555559;
  }
  * { margin: 0; padding: 0; box-sizing: border-box; }
  html, body { width: 1200px; height: 960px; overflow: hidden; }
  body { background: var(--bg); font-family: "Roboto", Arial, sans-serif; position: relative; }

  .card {
    position: absolute;
    width: 600px;
    height: 342px;
    overflow: hidden;
    box-shadow: 0 2px 5px rgba(0,0,0,0.25);
  }
  .card--front { left: 315px; top: 113px; background: linear-gradient(180deg, var(--slate-light), var(--slate)); }
  .card--back { left: 311px; top: 472px; background: var(--paper); }

  .front-panel { position: absolute; inset: 0; }

  .front-brand {
    position: absolute;
    left: 33px;
    top: 52px;
    color: var(--white);
    font-family: "Roboto Condensed", Arial, sans-serif;
    font-weight: 700;
    font-size: 21px;
    letter-spacing: 0.5px;
    text-transform: uppercase;
  }

  .contact {
    position: absolute;
    right: 37px;
    top: 163px;
    text-align: right;
    color: var(--white);
  }
  .contact__name {
    font-family: "Roboto Condensed", Arial, sans-serif;
    font-weight: 700;
    font-size: 21px;
    line-height: 24px;
  }
  .contact__role {
    font-family: "Roboto Condensed", Arial, sans-serif;
    font-weight: 500;
    font-size: 15px;
    line-height: 19px;
    margin-bottom: 9px;
  }
  .contact__line { font-size: 14px; line-height: 19px; }
  .contact__gap { margin-top: 7px; }

  .back-brand {
    position: absolute;
    left: 0; right: 0;
    top: 152px;
    text-align: center;
    color: var(--brand-blue);
    font-family: "Roboto Condensed", Arial, sans-serif;
    font-weight: 700;
    font-size: 30px;
    letter-spacing: 1px;
    text-transform: uppercase;
  }
  .back-web {
    position: absolute;
    left: 0; right: 0;
    top: 288px;
    text-align: center;
    color: var(--ink-grey);
    font-size: 14px;
    letter-spacing: 3.2px;
  }
</style>
</head>
<body>
  <section class="card card--front" aria-label="Card front">
    <svg class="front-panel" width="600" height="342" viewBox="0 0 600 342" aria-hidden="true">
      <path d="M228 342 C 258 210 300 90 372 0 L600 0 L600 342 Z" fill="var(--brand-blue)"/>
    </svg>

    <div class="front-brand">Tarrow Construct Works</div>

    <div class="contact">
      <div class="contact__name">LIAM HARGROVE</div>
      <div class="contact__role">CEO/FOUNDER</div>
      <div class="contact__line">1946 Wattle Grove Lane</div>
      <div class="contact__line">Penrith, NSW 2750</div>
      <div class="contact__line contact__gap">P: 0472 913 046</div>
      <div class="contact__line">admin@tarrowconstructworks.com.au</div>
      <div class="contact__line">www.tarrowconstructworks.com.au</div>
    </div>
  </section>

  <section class="card card--back" aria-label="Card back">
    <div class="back-brand">Tarrow Construct Works</div>
    <div class="back-web">www.tarrowconstructworks.com.au</div>
  </section>
</body>
</html>
```